81M business card

I need a business card for a life sciences consulting firm I started. The company name is 81M and the logo is attached. I am looking for something edgey and current but different from the blah standard business card.

Industry/Entity Type

Business

Requirements
Nice to have
• Both sides

```html
<!DOCTYPE html>
<html lang="en">
<head>
<meta charset="utf-8">
<title>81M Business Card</title>
<link rel="stylesheet" href="https://fonts.googleapis.com/css2?family=Ubuntu:wght@400;500;700&display=swap">
<style>
  :root {
    --backdrop: #d9d9d9;
    --card-white: #fbfbfb;
    --navy-dark: #0a2569;
    --navy-light: #1e4da6;
    --orange-light: #f7941d;
    --orange-dark: #e8380d;
    --brand-ink: #1b3f8f;
    --brand-accent: #f58220;
    --tagline-grey: #6d6d6d;
    --white: #ffffff;
  }
  * { margin: 0; padding: 0; box-sizing: border-box; }
  html, body { width: 1200px; height: 861px; overflow: hidden; }
  body {
    background: var(--backdrop);
    font-family: "Ubuntu", Arial, sans-serif;
    position: relative;
  }
  .card {
    position: absolute;
    top: 276px;
    width: 540px;
    height: 309px;
    background: var(--card-white);
    box-shadow: 0 10px 24px rgba(0,0,0,0.18);
    overflow: hidden;
  }
  .card--front { left: 45px; }
  .card--back { left: 615px; }
  .card__band { position: absolute; inset: 0; width: 540px; height: 309px; }

  .brand {
    position: absolute;
    display: flex;
    flex-direction: column;
  }
  .brand__row { display: flex; align-items: center; gap: 12px; }
  .brand__dot {
    width: 46px; height: 46px; border-radius: 50%;
    background: var(--brand-accent);
  }
  .brand__name {
    font-weight: 700;
    font-size: 44px;
    letter-spacing: 1px;
    color: var(--brand-ink);
    line-height: 1;
  }
  .brand__tagline {
    margin: 6px 0 0 58px;
    font-size: 10px;
    color: var(--tagline-grey);
    white-space: nowrap;
  }
  .card--front .brand { left: 30px; top: 44px; }
  .card--back .brand { left: 40px; top: 52px; }

  .holder {
    position: absolute;
    right: 26px;
    top: 142px;
    text-align: right;
    color: var(--white);
  }
  .holder__name { font-size: 24px; font-weight: 700; line-height: 1.2; }
  .holder__role { font-size: 15px; font-weight: 400; opacity: 0.9; }

  .contacts {
    position: absolute;
    left: 26px;
    top: 196px;
    list-style: none;
    color: var(--white);
    font-size: 13px;
  }
  .contacts li { display: flex; align-items: center; gap: 7px; height: 21px; white-space: nowrap; }
  .contacts svg { width: 15px; height: 15px; flex: none; }

  .message {
    position: absolute;
    left: 0; right: 0;
    top: 184px;
    text-align: center;
    color: var(--white);
  }
  .message__slogan { font-size: 26px; font-weight: 700; white-space: nowrap; }
  .message__web { margin-top: 12px; font-size: 15px; font-weight: 400; }
</style>
</head>
<body>

  <section class="card card--front" aria-label="Card front">
    <svg class="card__band" viewBox="0 0 540 309" aria-hidden="true">
      <defs>
        <linearGradient id="navyBand" x1="0" y1="0" x2="1" y2="1">
          <stop offset="0" stop-color="#1e4da6"/>
          <stop offset="1" stop-color="#0a2569"/>
        </linearGradient>
      </defs>
      <path d="M0 132 H352 L372 112 L372 132 H540 V309 H0 Z" fill="url(#navyBand)"/>
    </svg>
    <div class="brand">
      <div class="brand__row">
        <span class="brand__dot"></span>
        <span class="brand__name">81M</span>
      </div>
      <span class="brand__tagline">life sciences advisory and project support</span>
    </div>
    <div class="holder">
      <div class="holder__name">Name Surname</div>
      <div class="holder__role">Director</div>
    </div>
    <ul class="contacts">
      <li>
        <svg viewBox="0 0 16 16"><circle cx="8" cy="8" r="7" fill="none" stroke="#fff" stroke-width="1.3"/><rect x="5.8" y="4" width="4.4" height="8" rx="0.8" fill="none" stroke="#fff" stroke-width="1.1"/></svg>
        0123 456 789
      </li>
      <li>
        <svg viewBox="0 0 16 16"><circle cx="8" cy="8" r="7" fill="none" stroke="#fff" stroke-width="1.3"/><rect x="4" y="5.3" width="8" height="5.4" fill="none" stroke="#fff" stroke-width="1.1"/><path d="M4 5.3 L8 8.5 L12 5.3" fill="none" stroke="#fff" stroke-width="1.1"/></svg>
        name@81m.com
      </li>
      <li>
        <svg viewBox="0 0 16 16"><circle cx="8" cy="8" r="7" fill="none" stroke="#fff" stroke-width="1.3"/><circle cx="8" cy="8" r="3.8" fill="none" stroke="#fff" stroke-width="1"/><path d="M4.2 8 H11.8 M8 4.2 V11.8" stroke="#fff" stroke-width="1"/></svg>
        www.81m.com
      </li>
      <li>
        <svg viewBox="0 0 16 16"><circle cx="8" cy="8" r="7" fill="none" stroke="#fff" stroke-width="1.3"/><path d="M8 12.5 C6 10 5.2 8.6 5.2 7.2 A2.8 2.8 0 0 1 10.8 7.2 C10.8 8.6 10 10 8 12.5 Z" fill="none" stroke="#fff" stroke-width="1.1"/><circle cx="8" cy="7.2" r="1" fill="#fff"/></svg>
        Lorem Street, Ipsum City, Sit Amet
      </li>
    </ul>
  </section>

  <section class="card card--back" aria-label="Card back">
    <svg class="card__band" viewBox="0 0 540 309" aria-hidden="true">
      <defs>
        <linearGradient id="orangeBand" x1="0" y1="1" x2="1" y2="0">
          <stop offset="0" stop-color="#f7941d"/>
          <stop offset="1" stop-color="#e8380d"/>
        </linearGradient>
      </defs>
      <path d="M0 140 H214 L234 120 L234 140 H540 V309 H0 Z" fill="url(#orangeBand)"/>
    </svg>
    <div class="brand">
      <div class="brand__row">
        <span class="brand__dot"></span>
        <span class="brand__name">81M</span>
      </div>
      <span class="brand__tagline">life sciences advisory and project support</span>
    </div>
    <div class="message">
      <div class="message__slogan">Your company slogan will go here.</div>
      <div class="message__web">www.yourcompany.com</div>
    </div>
  </section>

</body>
</html>
```